New Business Card Design For Re-Branded Company (New Logo)

We recently switched our DBA and had a new logo designed. We now need new business cards made around our new logo. We would like to stick with the color scheme in our logo: White, Orange, and Blue. We want to see original bold designs that reflect our position in the solar energy sector but we prefer simple over complicated.

We are curious about vertical designs so if you can translate your design onto a vertical layout we would be open to look at it. We especially like a few designs we have seen on here that are vertical with a black or very dark gray background. They have our logo on one side and then the normal vertical business card on the other side.

I have included a screenshot of one of the samples we like, labeled sample.jpg and a file we were given as an example of our logo on a dark background.

At the same time we are satisfied to stay with what we have always had in a horizontal format. If it's not a lot of extra work for you, designs that are submitted in both horizontal and vertical formats will be greatly appreciated.

Please submit your original, bold, clean designs for consideration. Contact us with any questions or comments that may arise.

Thank you and Good Luck,

KP

```html
<!DOCTYPE html>
<html lang="en">
<head>
<meta charset="utf-8">
<title>Kestrel Power – Business Card</title>
<link rel="stylesheet" href="https://fonts.googleapis.com/css2?family=Montserrat:wght@600&family=Lato:wght@400;700&display=swap">
<style>
  :root {
    --stage: #2b2b2d;
    --blue-light: #2a8fd6;
    --blue-mid: #1676c2;
    --blue-deep: #0d5a9e;
    --orange: #e8741e;
    --white: #ffffff;
    --soft-white: #e6f0fa;
  }
  * { margin: 0; padding: 0; box-sizing: border-box; }
  html, body {
    width: 1200px;
    height: 997px;
    overflow: hidden;
    background: var(--stage);
  }
  .stage {
    width: 1200px;
    height: 997px;
    display: flex;
    flex-direction: column;
    align-items: center;
    justify-content: center;
    gap: 44px;
  }
  .card {
    position: relative;
    width: 700px;
    height: 420px;
    border-radius: 22px;
    overflow: hidden;
    box-shadow: 0 18px 40px rgba(0, 0, 0, 0.45);
  }
  .card-pattern {
    position: absolute;
    inset: 0;
    background:
      radial-gradient(ellipse at 30% 25%, rgba(255,255,255,0.12), transparent 60%),
      linear-gradient(135deg, var(--blue-light) 0%, var(--blue-mid) 50%, var(--blue-deep) 100%);
  }
  .brand {
    position: absolute;
    display: flex;
    flex-direction: column;
    align-items: center;
    gap: 14px;
  }
  .brand-dot {
    width: 56px;
    height: 56px;
    border-radius: 50%;
    border: 5px solid var(--white);
  }
  .brand-name {
    font-family: "Montserrat", sans-serif;
    font-weight: 600;
    font-size: 44px;
    letter-spacing: 1px;
    color: var(--white);
    white-space: nowrap;
  }
  .card-back .brand {
    left: 50%;
    top: 50%;
    transform: translate(-50%, -50%);
  }
  .card-front .brand {
    left: 56px;
    top: 130px;
  }
  .holder {
    position: absolute;
    right: 40px;
    top: 34px;
    text-align: right;
    font-family: "Lato", sans-serif;
  }
  .holder-name {
    font-weight: 700;
    font-size: 22px;
    color: var(--white);
  }
  .holder-role {
    font-size: 14px;
    color: var(--orange);
    margin-top: 2px;
  }
  .contact {
    position: absolute;
    right: 40px;
    bottom: 52px;
    font-family: "Lato", sans-serif;
    color: var(--soft-white);
    font-size: 15px;
    text-align: right;
  }
  .contact-company {
    font-size: 18px;
    margin-bottom: 8px;
  }
  .contact-row {
    display: flex;
    align-items: center;
    justify-content: flex-end;
    gap: 10px;
    line-height: 26px;
  }
  .contact-address {
    color: var(--orange);
    font-weight: 700;
    margin-right: 16px;
  }
  .icon {
    width: 14px;
    height: 14px;
    flex: none;
  }
</style>
</head>
<body>
<main class="stage">

  <section class="card card-back" aria-label="Card back">
    <div class="card-pattern" role="img" aria-label="Blue low-poly faceted triangle background"></div>
    <div class="brand">
      <span class="brand-dot"></span>
      <span class="brand-name">KESTREL POWER</span>
    </div>
  </section>

  <section class="card card-front" aria-label="Card front">
    <div class="card-pattern" role="img" aria-label="Blue low-poly faceted triangle background"></div>

    <div class="brand">
      <span class="brand-dot"></span>
      <span class="brand-name">KESTREL POWER</span>
    </div>

    <div class="holder">
      <p class="holder-name">Daniel Hovland</p>
      <p class="holder-role">Owner / Founder</p>
    </div>

    <div class="contact">
      <p class="contact-company">KESTREL POWER</p>
      <p class="contact-row">
        <span class="contact-address">Fjordgata 12, 3110 Lindvik, Norway</span>
        <span>+47 400 12 345</span>
        <svg class="icon" viewBox="0 0 14 14" aria-hidden="true">
          <rect x="3.5" y="1" width="7" height="12" rx="1.5" fill="none" stroke="var(--orange)" stroke-width="1.4"/>
          <line x1="6" y1="11" x2="8" y2="11" stroke="var(--orange)" stroke-width="1.2"/>
        </svg>
      </p>
      <p class="contact-row">
        <span>info@kestrelpower.no</span>
        <svg class="icon" viewBox="0 0 14 14" aria-hidden="true">
          <rect x="1" y="3" width="12" height="8" rx="1" fill="var(--orange)"/>
          <polyline points="1.5,3.5 7,8 12.5,3.5" fill="none" stroke="var(--blue-mid)" stroke-width="1.2"/>
        </svg>
      </p>
      <p class="contact-row">
        <span>www.kestrelpower.no</span>
        <svg class="icon" viewBox="0 0 14 14" aria-hidden="true">
          <circle cx="7" cy="7" r="5.5" fill="none" stroke="var(--orange)" stroke-width="1.4"/>
          <line x1="1.5" y1="7" x2="12.5" y2="7" stroke="var(--orange)" stroke-width="1.1"/>
          <ellipse cx="7" cy="7" rx="2.3" ry="5.5" fill="none" stroke="var(--orange)" stroke-width="1.1"/>
        </svg>
      </p>
    </div>
  </section>

</main>
</body>
</html>
```